Illustrated restaurant promotional posters

We need series of 5 promotional posters for a restaurant, each one promoting a different special across the week. The text for each poster must be included and is in the file attached to this brief, but the design should only be treated as a draft idea for what we are looking for (we are flexible). We're looking to add illustrations to these posters, which may or may not require a complete re-imagining. The restaurant serves American BBQ with a latin twist, is smart casual, and the poster should reflect a welcoming, casual, but also elegant establishment. Images of food and the venue can be found here https://www.cedarforkgrillhouse.com/

Target Market(s)

18 to 65, broad range of people, local restaurant, people popping in for a quick bite, and also celebrating main events

Industry/Entity Type

Restaurant

Font styles to use
Sans Serif

Colors
0054AA
0677BA
7BADD7
CADEEF
E8F1F8
EB3D1F
EC4F4E
F09395
F8D3D4
FCEDEE

Requirements
Must have
• Each poster must contain the text that is in the attached draft poster, illustration
Nice to have
• Colours similar to what is in attached file, though open to other otions

```html
<!DOCTYPE html>
<html lang="en">
<head>
<meta charset="utf-8">
<title>$10 Cocktails – Cedar Fork Grill House</title>
<link href="https://fonts.googleapis.com/css2?family=Bebas+Neue&family=Great+Vibes&display=swap" rel="stylesheet">
<style>
  :root{
    --board:#221e2c;
    --board-ghost:#262f45;
    --board-ghost-soft:#2a3043;
    --poster-top:#ff3512;
    --poster-mid:#ff6a52;
    --photo-red:#b8201a;
    --photo-amber:#e8902a;
    --photo-wood:#7a3a16;
    --white:#ffffff;
  }
  *{margin:0;padding:0;box-sizing:border-box}
  html,body{width:848px;height:1200px;overflow:hidden;background:var(--board)}
  .board{position:relative;width:848px;height:1200px;overflow:hidden;background:var(--board)}

  .board-backdrop{
    position:absolute;left:0;right:0;top:740px;bottom:0;
    background:radial-gradient(ellipse at 50% 60%, #2b2f42 0%, #232232 55%, var(--board) 85%);
  }
  .ghost-price{
    position:absolute;left:0;right:0;top:62px;text-align:center;
    font-family:"Bebas Neue",sans-serif;font-size:250px;line-height:1;
    color:var(--board-ghost);letter-spacing:2px;
  }
  .series-title{
    position:absolute;left:0;right:0;top:98px;text-align:center;
    font-family:"Great Vibes",cursive;font-weight:400;font-size:132px;line-height:1;
    word-spacing:14px;color:var(--white);
  }

  .poster{
    position:absolute;left:135px;top:239px;width:579px;height:819px;overflow:hidden;
    background:linear-gradient(180deg,var(--poster-top) 0%,#ff4a2a 30%,var(--poster-mid) 55%,#ff5a3e 70%);
    box-shadow:0 6px 22px rgba(0,0,0,.55);
  }
  .poster-photo{
    position:absolute;left:0;right:0;top:400px;bottom:0;
    background:
      radial-gradient(ellipse 34% 40% at 28% 68%, var(--photo-red) 0%, rgba(184,32,26,.8) 55%, transparent 75%),
      radial-gradient(ellipse 32% 42% at 76% 70%, var(--photo-amber) 0%, rgba(232,144,42,.8) 55%, transparent 78%),
      linear-gradient(180deg, rgba(255,106,82,0) 0%, rgba(230,90,60,.6) 35%, var(--photo-wood) 100%);
  }
  .poster-copy{position:absolute;left:0;right:0;top:0;text-align:center;color:var(--white);font-family:"Bebas Neue",sans-serif}
  .price{position:absolute;left:0;right:0;top:46px;font-size:196px;line-height:1;letter-spacing:1px}
  .item{position:absolute;left:0;right:0;top:220px;font-size:80px;line-height:1;letter-spacing:2px}
  .days{position:absolute;left:0;right:0;top:310px;font-size:84px;line-height:.87;letter-spacing:3px}

  .brand{position:absolute;left:0;right:0;top:712px;text-align:center;color:var(--white)}
  .brand-name{font-family:"Bebas Neue",sans-serif;font-weight:400;font-size:30px;letter-spacing:1px;line-height:1}
  .social{display:flex;justify-content:center;gap:11px;margin-top:18px}
  .social-dot{width:26px;height:26px;border-radius:50%;background:var(--white);display:flex;align-items:center;justify-content:center}

  .ghost-brand{position:absolute;left:0;right:0;top:1058px;text-align:center;color:var(--board-ghost-soft)}
  .ghost-brand .brand-name{font-size:40px;letter-spacing:1px}
  .ghost-brand .social{gap:14px;margin-top:28px}
  .ghost-brand .social-dot{width:40px;height:40px;background:var(--board-ghost-soft)}
</style>
</head>
<body>
<div class="board">
  <div class="board-backdrop" role="img" aria-label="Dimmed photo of cocktails on a wooden table"></div>
  <div class="ghost-price" aria-hidden="true">$10</div>
  <h1 class="series-title">Poster 2</h1>

  <section class="poster">
    <div class="poster-photo" role="img" aria-label="Photo of a red rosemary cocktail and a sugar-rimmed apple cocktail on a wooden table"></div>
    <div class="poster-copy">
      <p class="price">$10</p>
      <p class="item">COCKTAILS</p>
      <p class="days">WEDNESDAY<br>AND<br>THURSDAY</p>
    </div>
    <div class="brand">
      <p class="brand-name">CEDAR FORK GRILL HOUSE</p>
      <div class="social">
        <span class="social-dot" aria-label="Social page"></span>
        <span class="social-dot" aria-label="Photo feed"></span>
        <span class="social-dot" aria-label="Email">
          <svg width="16" height="12" viewBox="0 0 16 12"><rect x="1" y="1" width="14" height="10" fill="none" stroke="#ff4a2a" stroke-width="1.4"/><path d="M1 1 L8 7 L15 1" fill="none" stroke="#ff4a2a" stroke-width="1.4"/></svg>
        </span>
      </div>
    </div>
  </section>

  <div class="ghost-brand" aria-hidden="true">
    <p class="brand-name">CEDAR FORK GRILL HOUSE</p>
    <div class="social">
      <span class="social-dot"></span>
      <span class="social-dot"></span>
      <span class="social-dot">
        <svg width="24" height="18" viewBox="0 0 16 12"><rect x="1" y="1" width="14" height="10" fill="none" stroke="#221e2c" stroke-width="1.2"/><path d="M1 1 L8 7 L15 1" fill="none" stroke="#221e2c" stroke-width="1.2"/></svg>
      </span>
    </div>
  </div>
</div>
</body>
</html>
```